Unique Concept Design to Website Needed

Please see the attached folder. I have random images,etc but most importantly I have an attached image I was working on as a concept of a website. The brown background with blue and brown squares. logo in upper left and a little about me and then the squares would have names on them to lead to a section of the website with more info. I envision, when you mouse over a square, an image would appear so I attached random images here as well. Maybe some squares already have some images too.
- I want simple fonts. i like CLEAN, fonts
- text should be minimal. i am changing my site to less text, more powerful, bolder, larger lines with less content
- i am not sold on brown as the secondary color. i like blue but maybe grays, whites, offwhite scales or some other colors
-i have another graphic in there too
-you can see from my mock what company i am. please feel free to look me up and pull any portfolio , info , etc content to help make a great mock.
Do something cool!

```html
<!DOCTYPE html>
<html lang="en">
<head>
<meta charset="utf-8">
<title>Brisk internet solutions</title>
<link rel="stylesheet" href="https://fonts.googleapis.com/css2?family=Arimo:wght@400;700&display=swap">
<style>
  :root {
    --tile: #f9b13c;
    --tile-deep: #f0a52d;
    --tile-faint: rgba(240, 170, 60, 0.35);
    --tile-beige: rgba(238, 215, 160, 0.75);
    --ink: #1c1c1c;
    --tagline-grey: #4a4a4a;
    --footer-bg: #121212;
    --footer-chip: #1c1c1c;
    --footer-text: #ffffff;
    --chat-blue: #5f8fb3;
  }
  * { box-sizing: border-box; margin: 0; padding: 0; }
  html, body { width: 1200px; height: 558px; overflow: hidden; }
  body { position: relative; font-family: "Arimo", Arial, sans-serif; color: var(--ink); background: #fff; }

  .office-scene {
    position: absolute; inset: 0 0 36px 0;
    background:
      linear-gradient(180deg, rgba(255,255,255,0) 55%, rgba(20,20,20,0.75) 100%),
      linear-gradient(90deg, #fafafa 0%, #ececec 22%, #bdbdbd 40%, #8c8c8c 58%, #9a9a9a 72%, #5e5e5e 88%, #7a7a7a 100%);
  }

  .brand { position: absolute; left: 50px; top: 22px; width: 260px; height: 85px; }
  .brand-name { font-family: "Arimo", Arial, sans-serif; font-weight: 400; font-size: 46px; line-height: 1; color: var(--tagline-grey); }
  .brand-tagline { position: absolute; left: 49px; top: 65px; white-space: nowrap; font-size: 20px; color: var(--tagline-grey); letter-spacing: 0.3px; }

  .intro {
    position: absolute; left: 35px; top: 115px; width: 271px; height: 143px;
    background: var(--tile); padding: 22px 18px 0 21px;
    font-size: 12.6px; line-height: 17px; letter-spacing: 0.4px; color: var(--ink);
  }
  .intro-name { font-size: 15.5px; letter-spacing: 0.8px; }
  .intro-more { position: absolute; right: 14px; bottom: 12px; font-size: 13px; letter-spacing: 0.5px; }

  .tile {
    position: absolute; width: 116px; height: 116px;
    background: var(--tile); opacity: 0.93;
    display: flex; align-items: center; justify-content: center;
    font-size: 17px; letter-spacing: 1.3px; color: var(--ink); text-decoration: none;
  }
  .tile--deep { background: var(--tile-deep); }
  .tile-ghost { position: absolute; background: var(--tile-faint); }
  .tile-ghost--beige { background: var(--tile-beige); }

  .site-footer {
    position: absolute; left: 0; bottom: 0; width: 1200px; height: 36px;
    background: var(--footer-bg); color: var(--footer-text);
    font-weight: 700; font-size: 11.5px; letter-spacing: 0.2px;
  }
  .social { position: absolute; left: 50px; top: 9px; display: flex; gap: 10px; }
  .social-square { width: 19px; height: 19px; background: #5a5a5a; border-radius: 2px; }
  .phone { position: absolute; left: 137px; top: 0; height: 36px; padding: 0 14px 0 10px; background: var(--footer-chip); display: flex; align-items: center; gap: 6px; }
  .address { position: absolute; left: 782px; top: 0; height: 36px; display: flex; align-items: center; gap: 7px; }

  .live-chat { position: absolute; left: 1089px; top: 466px; width: 76px; height: 78px; z-index: 2; }
</style>
</head>
<body>
  <div class="office-scene" role="img" aria-label="Photo of a consultant working on a laptop in a sunlit office with chairs and a desk"></div>

  <header class="brand">
    <div class="brand-name">Brisk</div>
    <div class="brand-tagline">internet solutions</div>
  </header>

  <section class="intro">
    <p><span class="intro-name">Daniel Morrow</span> is a digital marketing consulting developing websites, promoting websites, and creating degital video &amp; media for business.</p>
    <a class="intro-more">view more v</a>
  </section>

  <div class="tile-ghost" style="left:320px;top:212px;width:114px;height:115px;"></div>
  <div class="tile-ghost" style="left:451px;top:278px;width:116px;height:118px;"></div>
  <div class="tile-ghost" style="left:864px;top:198px;width:116px;height:116px;"></div>
  <div class="tile-ghost tile-ghost--beige" style="left:997px;top:0;width:115px;height:108px;"></div>
  <div class="tile-ghost" style="left:787px;top:0;width:60px;height:77px;"></div>

  <nav>
    <a class="tile" style="left:451px;top:135px;">about</a>
    <a class="tile" style="left:592px;top:47px;">design</a>
    <a class="tile" style="left:592px;top:182px;">promo</a>
    <a class="tile" style="left:592px;top:328px;">web</a>
    <a class="tile" style="left:732px;top:117px;">videos</a>
    <a class="tile" style="left:732px;top:269px;">portfolio</a>
    <a class="tile" style="left:866px;top:58px;">testimonials</a>
    <a class="tile tile--deep" style="left:866px;top:338px;">pay online</a>
  </nav>

  <footer class="site-footer">
    <div class="social">
      <span class="social-square"></span>
      <span class="social-square"></span>
      <span class="social-square"></span>
    </div>
    <div class="phone">
      <svg width="11" height="13" viewBox="0 0 11 13"><path d="M2 1 L4 0.5 L5 4 L3.5 5 Q4.5 8 7 9.5 L8 8 L11 9.5 L10 12 Q4 12 1 5 Q0.8 2.5 2 1 Z" fill="#fff"/></svg>
      <span>800.555.0142</span>
    </div>
    <div class="address">
      <svg width="9" height="13" viewBox="0 0 9 13"><path d="M4.5 0 A4.5 4.5 0 0 1 9 4.5 C9 7.5 4.5 13 4.5 13 C4.5 13 0 7.5 0 4.5 A4.5 4.5 0 0 1 4.5 0 Z" fill="#fff"/><circle cx="4.5" cy="4.5" r="1.7" fill="var(--footer-bg)"/></svg>
      <span>240 HARBOR ST. SUITE 12 LAKEPORT, MI 48059</span>
    </div>
  </footer>

  <svg class="live-chat" viewBox="0 0 78 80" aria-label="live chat">
    <circle cx="39" cy="35" r="35" fill="var(--chat-blue)"/>
    <path d="M12 56 L6 78 L30 66 Z" fill="var(--chat-blue)"/>
    <circle cx="40" cy="34" r="28" fill="#fff"/>
    <text x="40" y="31" text-anchor="middle" font-family="Arimo, Arial, sans-serif" font-size="14" fill="#333">live</text>
    <text x="40" y="47" text-anchor="middle" font-family="Arimo, Arial, sans-serif" font-size="14" fill="#333">chat</text>
  </svg>
</body>
</html>
```